New business card design needed for Trucking/Staffing company!

I am looking for a business card design. The business name is Harbor Lane Freightworks, LLC. This company is a staffing company for commercial drivers/truck drivers. Most of our customers are trucking/supply companies. Our colors are blue/black/white/grey. The info I have on my current business cards is
-Spot for a name
-2 lines for an address
-3 lines for Office, cell, and fax
-email
-website(currently on backside of card with logo but can go anywhere)
Updates

Project Deadline Extended
Reason: Open to more designs

Target Market(s)

Trucking companies, building supply companies

Industry/Entity Type

Business

Contact Information for Business Card

Edgy but professional

Font styles to use
Other font styles liked:
• Open to suggestions

Colors
0555a3
000000
ffffff
9d9d9d

Requirements
Must have
• Must have the logo incorporated

```html
<!DOCTYPE html>
<html lang="en">
<head>
<meta charset="utf-8">
<title>Harbor Lane Freightworks – Business Card</title>
<link rel="stylesheet" href="https://fonts.googleapis.com/css2?family=Lato:wght@400;700;900&display=swap">
<style>
  :root {
    --backdrop: #b4b4b4;
    --card-white: #ffffff;
    --card-dark: #231f20;
    --brand-blue: #2a3192;
    --ink: #1c1c1c;
    --light-text: #ffffff;
    --rule-grey: #9d9d9d;
  }
  * { margin: 0; padding: 0; box-sizing: border-box; }
  html, body { width: 1200px; height: 750px; overflow: hidden; }
  body {
    background: var(--backdrop);
    font-family: "Lato", sans-serif;
    position: relative;
  }
  .card {
    position: absolute;
    top: 218px;
    width: 492px;
    height: 282px;
    overflow: hidden;
  }
  .card--front { left: 91px; background: var(--card-white); }
  .card--back { left: 620px; background: var(--card-dark); }

  .front-band {
    position: absolute;
    left: 0; right: 0; top: 148px; bottom: 0;
    background: var(--card-dark);
  }
  .front-accent {
    position: absolute;
    left: 0; top: 146px;
    width: 492px; height: 12px;
  }
  .wordmark {
    position: absolute;
    left: 26px; top: 44px;
    display: flex; align-items: center; gap: 8px;
    color: var(--brand-blue);
    font-weight: 900;
    font-size: 17px;
    letter-spacing: 0.3px;
  }
  .wordmark__square {
    width: 14px; height: 14px;
    background: var(--brand-blue);
  }
  .person {
    position: absolute;
    right: 23px; top: 29px;
    text-align: right;
  }
  .person__name {
    color: var(--brand-blue);
    font-weight: 700;
    font-size: 18.5px;
    line-height: 22px;
  }
  .person__title {
    color: var(--ink);
    font-size: 13.5px;
    line-height: 17px;
  }
  .address {
    position: absolute;
    left: 24px; top: 190px;
    color: var(--light-text);
    font-size: 13.5px;
    line-height: 16.5px;
    letter-spacing: 0.4px;
  }
  .address__company { font-weight: 700; letter-spacing: 0; }
  .contacts {
    position: absolute;
    right: 23px; top: 184px;
    list-style: none;
    color: var(--light-text);
    font-size: 12.5px;
    line-height: 15.3px;
  }
  .contacts li { display: flex; align-items: center; gap: 5px; }
  .contacts svg { width: 11px; height: 11px; flex: none; }

  .back-wordmark {
    position: absolute;
    left: 0; right: 0; top: 112px;
    text-align: center;
    color: var(--light-text);
    font-weight: 900;
    font-size: 27px;
    letter-spacing: 0.5px;
  }
  .back-web {
    position: absolute;
    left: 90px; right: 90px; top: 242px;
    display: flex; align-items: center; gap: 4px;
    color: var(--light-text);
    font-size: 12.5px;
  }
  .back-web__rule { flex: 1; height: 1px; background: var(--light-text); opacity: 0.8; }
</style>
</head>
<body>
  <section class="card card--front">
    <div class="wordmark"><span class="wordmark__square"></span>Harbor Lane Freightworks</div>
    <div class="person">
      <p class="person__name">Daniel Mercer</p>
      <p class="person__title">President</p>
    </div>
    <div class="front-band"></div>
    <svg class="front-accent" viewBox="0 0 492 12" aria-hidden="true">
      <polygon points="246,2 492,2 492,9 254,9" fill="var(--brand-blue)"/>
      <polyline points="246,2 254,10 492,10" fill="none" stroke="#ffffff" stroke-width="0.8"/>
    </svg>
    <div class="address">
      <p class="address__company">Harbor Lane Freightworks</p>
      <p>Po Box 417</p>
      <p>Harbor Lane Freightworks, LLC</p>
    </div>
    <ul class="contacts">
      <li><svg viewBox="0 0 12 12"><rect x="3" y="0.5" width="6" height="11" rx="1" fill="none" stroke="#fff" stroke-width="1.2"/><rect x="5" y="9" width="2" height="1" fill="#fff"/></svg>01230004567</li>
      <li><svg viewBox="0 0 12 12"><path d="M1 4 Q6 0 11 4 L10 5.5 L8 4.5 L4 4.5 L2 5.5 Z" fill="#fff"/><rect x="2.5" y="6" width="7" height="5" rx="1" fill="#fff"/></svg>+0987000123</li>
      <li><svg viewBox="0 0 12 12"><rect x="3" y="0.5" width="6" height="3" fill="#fff"/><rect x="0.5" y="4" width="11" height="5" rx="1" fill="#fff"/><rect x="3" y="7.5" width="6" height="4" fill="#fff" stroke="#231f20" stroke-width="0.8"/></svg>+0987000123</li>
      <li><svg viewBox="0 0 12 12"><rect x="0.5" y="2" width="11" height="8" fill="#fff"/><polyline points="0.5,2 6,7 11.5,2" fill="none" stroke="#231f20" stroke-width="1"/></svg>info@harborlanefreight.com</li>
      <li><svg viewBox="0 0 12 12"><g fill="none" stroke="#fff" stroke-width="0.9"><circle cx="6" cy="6" r="5.3"/><ellipse cx="6" cy="6" rx="2.3" ry="5.3"/><line x1="0.7" y1="6" x2="11.3" y2="6"/><line x1="1.5" y1="3.5" x2="10.5" y2="3.5"/><line x1="1.5" y1="8.5" x2="10.5" y2="8.5"/></g></svg>www.harborlanefreight.com</li>
    </ul>
  </section>

  <section class="card card--back">
    <p class="back-wordmark">Harbor Lane Freightworks</p>
    <div class="back-web">
      <span class="back-web__rule"></span>
      <span>www.harborlanefreight.com</span>
      <span class="back-web__rule"></span>
    </div>
  </section>
</body>
</html>
```